Funky Entertainment and Music Solutions Company

Marlo Tindell Entertainment (www.marlotindell-example.com) needs a fresh new face. We are in Entertainment and Music Solutions for corporate and private functions providing a very hands-on and customer focused premium approach to our client's entertainment needs.

Current Logo:
It's the MARLO TINDELL ENTERTAINMENT found on our website above

What do we do?
We advise, organise, source and manage your event (big or small) from a string quartet for a cocktail party to pre-dinner entertainment and big band entertainment for the corporate Christmas Party.

Our Objective:
To become the main Entertainment and Music Solutions provider to large Australia/Asia Pac corporations as well as private parties.

Look and Feel?
We have recently released our new services booklet found here: http://www.pagewhirl-example.com/3A51B2C0F4D/q2mz84xr and whilst we don't want the site to look like a rainbow, it should incorporate the sleek, funky, clean look that we're tying to achieve.

Main pages we're after:
- Welcome/About Us
- Services (ie, strings, Covers Bands, Jazz Groups. All found in above booklet)
- Enquiry/Booking Page
- Gallery and Audio Page
Updates

This project now has a committed budget - submit away!
Thanks all!
Marlo Tindell Entertainment

Just a few updates on the project.
- We are trying to move away from what the current website offers. Our new client focus is corporate and private parties, not nightclubs. A great example are the images on the first and last pages of the flipbook: http://www.pagewhirl-example.com/3A51B2C0F4D/q2mz84xr
- Some websites that we like are found below. They are sleek, easy to navigate and not too much scrolling required. They incorporate a cool background with the floating ttext/images in the centre.
http://lanternhall-sf.example.com/
http://www.orbvale-example.com/
- Any questions, please ask!
Thanks and happy designing! :)

Industry/Entity Type

Entertainment

```html
<!DOCTYPE html>
<html lang="en">
<head>
<meta charset="utf-8">
<title>Marlo Tindell Entertainment</title>
<link rel="stylesheet" href="https://fonts.googleapis.com/css2?family=Arimo:wght@400;700&display=swap">
<style>
  :root {
    --black: #000000;
    --panel: rgba(16, 14, 20, 0.74);
    --panel-inner: rgba(6, 6, 8, 0.86);
    --plum: #8e2a6e;
    --nav-active: #c4419a;
    --white: #ffffff;
    --grey: #8a8a8a;
    --footer: rgba(8, 8, 12, 0.82);
  }
  * { margin: 0; padding: 0; box-sizing: border-box; }
  html, body { width: 1200px; height: 852px; overflow: hidden; background: var(--black); }
  body { font-family: "Arimo", Arial, sans-serif; color: var(--white); position: relative; }

  .site-header { position: absolute; left: 0; top: 0; width: 1200px; height: 172px; background: var(--black); }
  .header-portrait {
    position: absolute; left: 152px; top: 0; width: 210px; height: 172px;
    background: radial-gradient(ellipse at 55% 45%, #3a3246 0%, #1b1622 45%, #000 80%);
  }
  .brand-name {
    position: absolute; left: 372px; top: 60px;
    font-size: 38px; font-weight: 700; line-height: 44px; color: var(--white); white-space: nowrap;
  }
  .main-nav { position: absolute; top: 143px; left: 0; width: 1200px; height: 18px; }
  .main-nav a {
    position: absolute; top: 0; font-size: 13px; line-height: 16px; color: var(--white);
    text-decoration: none; white-space: nowrap;
  }
  .main-nav a.is-active { color: var(--nav-active); }

  .stage-backdrop {
    position: absolute; left: 0; top: 172px; width: 1200px; height: 680px;
    background:
      radial-gradient(circle at 82% 6%, rgba(140, 200, 80, 0.45) 0%, transparent 18%),
      radial-gradient(circle at 72% 92%, rgba(240, 230, 170, 0.45) 0%, transparent 10%),
      radial-gradient(ellipse at 8% 35%, rgba(150, 70, 60, 0.6) 0%, transparent 45%),
      radial-gradient(ellipse at 92% 40%, rgba(140, 70, 90, 0.6) 0%, transparent 45%),
      linear-gradient(180deg, #4a2636 0%, #4d3468 45%, #5c3688 75%, #30245a 100%);
  }

  .content-panel {
    position: absolute; left: 91px; top: 211px; width: 953px; height: 579px;
    background: var(--panel);
  }
  .content-inner {
    position: absolute; left: 155px; top: 240px; width: 811px; height: 530px;
    background: var(--panel-inner);
  }
  .welcome-title {
    position: absolute; left: 177px; top: 262px;
    font-size: 66px; font-weight: 400; line-height: 66px; color: var(--plum); white-space: nowrap;
  }
  .welcome-sub {
    position: absolute; left: 205px; top: 341px;
    font-size: 18.5px; font-weight: 400; line-height: 22px; color: var(--white); white-space: nowrap;
  }
  .welcome-divider { position: absolute; left: 566px; top: 268px; width: 1px; height: 94px; background: var(--grey); }
  .welcome-text {
    position: absolute; left: 594px; top: 282px; width: 360px;
    font-size: 15.5px; line-height: 22px; color: var(--white); white-space: nowrap;
  }
  .feature-photo {
    position: absolute; left: 196px; top: 385px; width: 735px; height: 357px;
    background:
      radial-gradient(ellipse at 68% 55%, #d96a6a 0%, #a83a3c 35%, transparent 65%),
      linear-gradient(110deg, #5a1212 0%, #b03a2e 30%, #3a0c0c 55%, #6a2020 100%);
  }

  .site-footer { position: absolute; left: 0; top: 817px; width: 1200px; height: 35px; background: var(--footer); }
  .copyright { position: absolute; left: 160px; top: 10px; font-size: 11px; line-height: 14px; color: var(--white); white-space: nowrap; }
  .social-links { position: absolute; left: 894px; top: 8px; display: flex; gap: 8px; }
  .social-links span { width: 18px; height: 18px; border-radius: 50%; background: var(--white); display: block; }
</style>
</head>
<body>
  <header class="site-header">
    <div class="header-portrait" role="img" aria-label="Photo of a saxophonist performing in sunglasses and a dark shirt"></div>
    <div class="brand-name">Marlo Tindell Entertainment</div>
    <nav class="main-nav">
      <a class="is-active" href="#" style="left:347px">Home</a>
      <a href="#" style="left:440px">About Us</a>
      <a href="#" style="left:553px">Services</a>
      <a href="#" style="left:664px">Gallery</a>
      <a href="#" style="left:765px">Contact</a>
      <a href="#" style="left:871px">BookNest</a>
    </nav>
  </header>

  <div class="stage-backdrop" role="img" aria-label="Blurred photo of an elegant function room with soft coloured stage lights"></div>

  <main>
    <div class="content-panel"></div>
    <div class="content-inner"></div>
    <h1 class="welcome-title">WELCOME</h1>
    <p class="welcome-sub">TO THE EVENT OF YOUR DREAMS</p>
    <div class="welcome-divider"></div>
    <p class="welcome-text">Entertainment &amp; Music Solutions&nbsp; - Strings,<br>jazz groups, covers bands, big bands.<br>Hands-on, premium service for corporate<br>functions and private parties.</p>
    <div class="feature-photo" role="img" aria-label="Photo of a saxophonist playing at a corporate function under warm red lighting"></div>
  </main>

  <footer class="site-footer">
    <p class="copyright">© 2023 by MARLO TINDELL ENTERTAINMENT.</p>
    <div class="social-links" aria-label="Social links">
      <span></span><span></span><span></span>
    </div>
  </footer>
</body>
</html>
```